Medical VIP club - small design

Please read the specs in a design brief attached. Also we don't have logo in a Vector format and attaching the only version we have.

Industry/Entity Type

Club

```html
<!DOCTYPE html>
<html lang="en">
<head>
<meta charset="utf-8">
<title>Velmora — VIP Medical Club</title>
<link rel="stylesheet" href="https://fonts.googleapis.com/css2?family=Arimo:wght@400;700&family=PT+Sans:wght@400;700&display=swap">
<style>
  :root {
    --page-bg: #5b4f34;
    --page-bg-dark: #4e4329;
    --cream: #f1efdf;
    --logo-cream: #f3efdc;
    --gold: #b8a960;
    --gold-light: #cbbd74;
    --nav-text: #4a3f2e;
    --nav-active: #241a10;
    --ink: #1f1a12;
    --caption-bg: #7b786f;
    --caption-active: #000000;
    --white: #ffffff;
    --overlay: rgba(30, 28, 26, 0.82);
    --btn-top: #f7b531;
    --btn-bottom: #e08a0e;
  }
  * { box-sizing: border-box; margin: 0; padding: 0; }
  html, body {
    width: 1200px; height: 854px; overflow: hidden;
  }
  body {
    font-family: "Arimo", Arial, sans-serif;
    background: radial-gradient(ellipse at 50% 40%, var(--page-bg) 0%, var(--page-bg-dark) 100%);
    position: relative;
  }
  .site-logo {
    position: absolute; display: flex; align-items: center; gap: 12px; white-space: nowrap;
  }
  .site-logo .mark {
    width: 34px; height: 34px; border-radius: 50%; background: var(--gold);
  }
  .site-logo .name {
    font-family: "Arimo", Arial, sans-serif; font-weight: 700;
    color: var(--logo-cream); letter-spacing: 0.5px;
  }
  .site-logo--header { left: 70px; top: 58px; }
  .site-logo--header .name { font-size: 50px; }
  .site-logo--footer { left: 936px; top: 786px; gap: 9px; }
  .site-logo--footer .mark { width: 24px; height: 24px; }
  .site-logo--footer .name { font-size: 36px; }

  .call-box { position: absolute; left: 914px; top: 51px; color: var(--white); white-space: nowrap; }
  .call-box .label { font-size: 15px; }
  .call-box .number {
    font-size: 41px; font-weight: 700; color: var(--ink); line-height: 1; margin-top: 3px;
    letter-spacing: -0.5px;
  }

  .main-nav {
    position: absolute; left: 65px; top: 131px; width: 1070px; height: 38px;
    background: var(--cream); display: flex; flex-wrap: nowrap; align-items: stretch;
    justify-content: space-between; padding: 0 7px;
  }
  .main-nav a {
    display: flex; align-items: center; padding: 0 20px; white-space: nowrap;
    font-size: 18px; color: var(--nav-text); text-decoration: none; text-transform: uppercase;
  }
  .main-nav a.active { background: var(--nav-active); color: var(--white); padding: 0 25px; }

  .hero {
    position: absolute; left: 65px; top: 169px; width: 1070px; height: 327px;
    background: linear-gradient(100deg, #cfcfcd 0%, #9c9c9a 30%, #6b6b69 55%, #3c3c3b 75%, #8a8a88 100%);
  }
  .hero-promo {
    position: absolute; left: 507px; top: 60px; width: 460px; height: 211px;
    background: var(--overlay); padding: 12px 27px;
  }
  .hero-promo h1 {
    font-family: "PT Sans", sans-serif; font-weight: 700; font-size: 49px;
    color: var(--gold-light); line-height: 1.1; white-space: nowrap;
  }
  .hero-promo p {
    color: var(--white); font-size: 15px; line-height: 22px; margin-top: 6px; width: 380px;
  }
  .register-btn {
    display: inline-block; margin-top: 21px; width: 245px; height: 54px; line-height: 50px;
    text-align: center; border-radius: 6px; border: 2px solid #c77a08;
    background: linear-gradient(var(--btn-top), var(--btn-bottom));
    font-family: "PT Sans", sans-serif; font-weight: 700; font-size: 25px;
    color: var(--ink); text-decoration: none; white-space: nowrap;
  }
  .slider-arrow {
    position: absolute; top: 298px; width: 44px; height: 70px; display: flex;
    align-items: center; justify-content: center;
  }
  .slider-arrow--prev { left: 44px; background: #5a5044; border-radius: 35px 0 0 35px; }
  .slider-arrow--next { left: 1112px; background: #2a2118; border-radius: 0 35px 35px 0; }

  .services {
    position: absolute; left: 65px; top: 496px; width: 1070px; height: 244px;
    background: var(--cream);
  }
  .service-list { position: absolute; left: 21px; top: 16px; display: flex; gap: 1px; }
  .service-card { width: 205px; }
  .service-card .photo { height: 167px; }
  .service-card .caption {
    height: 44px; background: var(--caption-bg); color: var(--white);
    font-family: "PT Sans", sans-serif; font-size: 16px; line-height: 15px;
    text-transform: uppercase; padding: 7px 0 0 20px; white-space: nowrap;
  }
  .service-card.active .caption { background: var(--caption-active); }

  .site-footer { position: absolute; left: 65px; top: 775px; white-space: nowrap; }
  .footer-nav { display: flex; align-items: center; gap: 9px; font-size: 13px; }
  .footer-nav a { color: var(--gold-light); text-decoration: none; }
  .footer-nav .sep { color: var(--gold); font-size: 12px; }
  .copyright {
    margin-top: 13px; font-size: 11px; color: var(--ink); display: flex; align-items: center; gap: 14px;
  }
  .copyright b { font-weight: 700; font-size: 12px; }
  .social { display: flex; gap: 4px; }
  .social span { width: 17px; height: 17px; background: #a99a6c; border-radius: 2px; }
</style>
</head>
<body>
  <header>
    <div class="site-logo site-logo--header">
      <span class="mark"></span><span class="name">velmora</span>
    </div>
    <div class="call-box">
      <div class="label">For more information Call Us</div>
      <div class="number">416-555-017</div>
    </div>
    <nav class="main-nav">
      <a class="active" href="#">Home</a>
      <a href="#">About Us</a>
      <a href="#">VIP Club</a>
      <a href="#">Services</a>
      <a href="#">Pacakge and Prices</a>
      <a href="#">Registration</a>
      <a href="#">Contact</a>
    </nav>
  </header>

  <section class="hero" role="img" aria-label="Photo of a modern grey lounge interior with a sofa and yellow cushions">
    <div class="hero-promo">
      <h1>VIP CLUB</h1>
      <p>Lorem Ipsum is simply dummy text of the printing and typesetting industry. Lorem Ipsum has been.</p>
      <a class="register-btn" href="#">REGISTER NOW!</a>
    </div>
  </section>
  <a class="slider-arrow slider-arrow--prev" href="#" aria-label="Previous slide">
    <svg width="14" height="18" viewBox="0 0 14 18"><path d="M11 2 L4 9 L11 16" fill="none" stroke="#d9d3c2" stroke-width="4"/></svg>
  </a>
  <a class="slider-arrow slider-arrow--next" href="#" aria-label="Next slide">
    <svg width="14" height="18" viewBox="0 0 14 18"><path d="M3 2 L10 9 L3 16" fill="none" stroke="#ffffff" stroke-width="4"/></svg>
  </a>

  <section class="services">
    <div class="service-list">
      <div class="service-card">
        <div class="photo" role="img" aria-label="Photo of an emergency direction sign" style="background:linear-gradient(160deg,#8d8477,#5f564b)"></div>
        <div class="caption">Emergency<br>Service Plan</div>
      </div>
      <div class="service-card active">
        <div class="photo" role="img" aria-label="Photo of a plane landing at sunset" style="background:linear-gradient(180deg,#f2b13a 0%,#d86a10 55%,#3a2410 100%)"></div>
        <div class="caption">Transportation<br>Service</div>
      </div>
      <div class="service-card">
        <div class="photo" role="img" aria-label="Photo of a hotel bedroom" style="background:linear-gradient(170deg,#a8876a,#5c3f2a)"></div>
        <div class="caption">Hotel<br>Service</div>
      </div>
      <div class="service-card">
        <div class="photo" role="img" aria-label="Photo of two doctors reviewing notes" style="background:linear-gradient(170deg,#d8cbb8,#8a7660)"></div>
        <div class="caption">Variety<br>of Doctors</div>
      </div>
      <div class="service-card">
        <div class="photo" role="img" aria-label="Photo of a membership application form" style="background:linear-gradient(170deg,#cbbba3,#8f7d66)"></div>
        <div class="caption">Becaome<br>a Member</div>
      </div>
    </div>
  </section>

  <footer class="site-footer">
    <nav class="footer-nav">
      <a href="#">Home</a><span class="sep">✷</span>
      <a href="#">About Us</a><span class="sep">✷</span>
      <a href="#">Vip Club</a><span class="sep">✷</span>
      <a href="#">Services</a><span class="sep">✷</span>
      <a href="#">Pacakge And Prices</a><span class="sep">✷</span>
      <a href="#">Registration</a><span class="sep">✷</span>
      <a href="#">Contact</a>
    </nav>
    <div class="copyright">
      <span>Copyright © 2010 <b>Velmora</b>. All Rights Reserved.</span>
      <span class="social"><span></span><span></span><span></span></span>
    </div>
  </footer>
  <div class="site-logo site-logo--footer">
    <span class="mark"></span><span class="name">velmora</span>
  </div>
</body>
</html>
```